Business card design needed

Please visit my website for the colors and logo design.

www.Lendarokqld.com.au

Business

Lendarok (Qld) Pty Ltd
Corwin Haske
Director
PO Box 418
Tallowin Qld 4287
PH: 1300648200
Fax: 07 5829 0317
Corwin@Lendarokqld.com.au

```html
<!DOCTYPE html>
<html lang="en">
<head>
<meta charset="utf-8">
<title>Lendarok business card options</title>
<link href="https://fonts.googleapis.com/css2?family=Arimo:wght@400;700&family=Questrial&display=swap" rel="stylesheet">
<style>
  :root {
    --bg: #eceded;
    --card: #ffffff;
    --blue-dark: #0a4fa0;
    --blue: #1a78d2;
    --blue-light: #3fa0ea;
    --green: #a6d161;
    --green-light: #cde59c;
    --ink: #2b2b2b;
    --ink-soft: #3d3d3d;
    --icon-blue: #1f5fa8;
    --icon-green: #8cbf3f;
  }
  * { margin: 0; padding: 0; box-sizing: border-box; }
  html, body { width: 1200px; height: 428px; overflow: hidden; background: var(--bg); }
  body { position: relative; font-family: "Questrial", "Century Gothic", sans-serif; color: var(--ink); }

  .option-number { position: absolute; font-family: "Arimo", Arial, sans-serif; font-size: 21px; color: #222; }
  .option-number.first { left: 48px; top: 93px; }
  .option-number.second { left: 616px; top: 88px; }

  .card { position: absolute; background: var(--card); box-shadow: 2px 5px 9px rgba(0,0,0,0.22); overflow: hidden; }
  .card.horizontal { left: 73px; top: 92px; width: 478px; height: 267px; }
  .card.vertical { left: 646px; top: 91px; width: 474px; height: 264px; }

  .brand-band { position: absolute; left: 0; top: 0; width: 100%; height: 96px;
    background: radial-gradient(ellipse at 50% 35%, var(--blue-light) 0%, var(--blue) 45%, var(--blue-dark) 100%); }
  .accent-rule { position: absolute; left: 0; top: 96px; width: 100%; height: 11px;
    background: linear-gradient(to bottom, var(--green-light) 0%, var(--green) 55%, #8fbf4a 100%); }
  .brand-panel { position: absolute; left: 0; top: 0; width: 181px; height: 100%;
    background: linear-gradient(to bottom, var(--blue-dark) 0%, var(--blue) 45%, var(--blue) 60%, var(--blue-dark) 100%); }
  .accent-bar { position: absolute; left: 187px; top: 0; width: 5px; height: 100%; background: var(--green); }

  .brand { position: absolute; color: #fff; font-family: "Arimo", Arial, sans-serif; text-align: center; }
  .brand .name { font-weight: 700; display: block; line-height: 1; letter-spacing: 0.5px; }
  .brand .entity { position: absolute; font-weight: 400; white-space: nowrap; }
  .brand .licence { display: block; font-weight: 400; white-space: nowrap; opacity: 0.85; }

  .horizontal .brand { left: 0; width: 478px; top: 22px; }
  .horizontal .brand .name { font-size: 40px; }
  .horizontal .brand .entity { right: 128px; top: -9px; font-size: 10px; }
  .horizontal .brand .licence { font-size: 9px; margin-top: 6px; }

  .vertical .brand { left: 0; width: 181px; top: 104px; }
  .vertical .brand .name { font-size: 29px; }
  .vertical .brand .entity { right: 14px; top: -8px; font-size: 7.5px; }
  .vertical .brand .licence { font-size: 6.5px; margin-top: 5px; }

  .person { position: absolute; }
  .person .person-name { font-family: "Arimo", Arial, sans-serif; font-weight: 700; font-size: 16px; color: var(--ink); line-height: 20px; display: block; }
  .person .person-role { font-family: "Arimo", Arial, sans-serif; font-size: 14.5px; color: var(--ink-soft); line-height: 20px; display: block; }
  .horizontal .person { right: 334px; top: 184px; text-align: right; }
  .vertical .person { left: 222px; top: 44px; }

  .divider { position: absolute; left: 158px; top: 118px; width: 2px; height: 146px;
    background: linear-gradient(to bottom, rgba(31,95,168,0) 0%, var(--icon-blue) 30%, var(--icon-blue) 70%, rgba(31,95,168,0) 100%); }

  .contacts { position: absolute; list-style: none; }
  .contacts li { display: flex; align-items: center; height: 21px; font-size: 14.5px; color: var(--ink-soft); white-space: nowrap; }
  .contacts svg { width: 14px; height: 14px; margin-right: 5px; flex: none; }
  .horizontal .contacts { left: 166px; top: 127px; }
  .vertical .contacts { left: 221px; top: 107px; }
  .horizontal .contacts svg { color: var(--icon-blue); }
  .vertical .contacts svg { color: var(--icon-green); }

  .address { position: absolute; font-size: 14.5px; color: var(--ink-soft); white-space: nowrap; line-height: 20px; }
  .horizontal .address { left: 171px; top: 218px; }
  .vertical .address { left: 225px; top: 197px; }
</style>
</head>
<body>

<svg width="0" height="0" style="position:absolute">
  <defs>
    <symbol id="icon-phone" viewBox="0 0 16 16"><path fill="currentColor" d="M3.2 1.5l2.3-.4 1.3 3.2-1.6 1.2c.7 1.7 2 3 3.6 3.8l1.3-1.6 3.2 1.3-.4 2.4c-.2.8-1 1.3-1.8 1.1C6.2 11.6 3.3 8.6 2.1 3.3c-.2-.8.3-1.6 1.1-1.8z"/></symbol>
    <symbol id="icon-fax" viewBox="0 0 16 16"><path fill="currentColor" d="M4 1h6l2 2v3H4z M2 6.5h12c.6 0 1 .4 1 1V13c0 .6-.4 1-1 1H2c-.6 0-1-.4-1-1V7.5c0-.6.4-1 1-1z"/><rect x="3" y="9" width="10" height="1.2" fill="#fff"/><rect x="3" y="11.2" width="10" height="1.2" fill="#fff"/></symbol>
    <symbol id="icon-mail" viewBox="0 0 16 16"><rect x="1.2" y="3.2" width="13.6" height="9.6" rx="1" fill="none" stroke="currentColor" stroke-width="1.3"/><path d="M1.5 3.8l6.5 5 6.5-5" fill="none" stroke="currentColor" stroke-width="1.3"/></symbol>
    <symbol id="icon-web" viewBox="0 0 16 16"><g fill="none" stroke="currentColor" stroke-width="1.1"><circle cx="8" cy="8" r="6.5"/><ellipse cx="8" cy="8" rx="3" ry="6.5"/><path d="M1.5 8h13M2.5 4.8h11M2.5 11.2h11"/></g></symbol>
  </defs>
</svg>

<span class="option-number first">1</span>
<section class="card horizontal">
  <div class="brand-band"></div>
  <div class="accent-rule"></div>
  <div class="brand">
    <span class="name">Lendarok</span>
    <span class="entity">(Qld) Pty Ltd</span>
    <span class="licence">Australian Credit Licence Number: 518273</span>
  </div>
  <div class="person">
    <span class="person-name">Corwin Haske</span>
    <span class="person-role">Director</span>
  </div>
  <div class="divider"></div>
  <ul class="contacts">
    <li><svg><use href="#icon-phone"/></svg>1300648200</li>
    <li><svg><use href="#icon-fax"/></svg>07 5829 0317</li>
    <li><svg><use href="#icon-mail"/></svg>Corwin@Lendarokqld.com.au</li>
    <li><svg><use href="#icon-web"/></svg>www.Lendarokqld.com.au</li>
  </ul>
  <p class="address">PO Box 418 Tallowin Qld 4287</p>
</section>

<span class="option-number second">2</span>
<section class="card vertical">
  <div class="brand-panel"></div>
  <div class="accent-bar"></div>
  <div class="brand">
    <span class="name">Lendarok</span>
    <span class="entity">(Qld) Pty Ltd</span>
    <span class="licence">Australian Credit Licence Number: 518273</span>
  </div>
  <div class="person">
    <span class="person-name">Corwin Haske</span>
    <span class="person-role">Director</span>
  </div>
  <ul class="contacts">
    <li><svg><use href="#icon-phone"/></svg>1300648200</li>
    <li><svg><use href="#icon-fax"/></svg>07 5829 0317</li>
    <li><svg><use href="#icon-mail"/></svg>Corwin@Lendarokqld.com.au</li>
    <li><svg><use href="#icon-web"/></svg>www.Lendarokqld.com.au</li>
  </ul>
  <p class="address">PO Box 418 Tallowin Qld 4287</p>
</section>

</body>
</html>
```